Website design for labour force (commercial truck driver) company

Looking for a Wordpress template (or design files in conjunction with a free Wordpress template).
Company tag line:
Tenvora – On Demand, Professional Drivers
Real Drivers | Real Standards | Real Results
Logo design has already been completed and is attached

Company provides contract drivers to trucking companies. Target market is both the trucking companies looking for drivers and drivers looking for work.
Design to encompass header / footer and basic page design, navigation menu, home page, contact page. Customer will add content and additional pages over time.

```html
<!DOCTYPE html>
<html lang="en">
<head>
<meta charset="utf-8">
<title>Tenvora – On Demand, Professional Drivers</title>
<link href="https://fonts.googleapis.com/css2?family=Inter:wght@300;400;500;600;700&display=swap" rel="stylesheet">
<style>
:root{
  --green:#12876a;
  --mint:#0bd98f;
  --ink:#111418;
  --soft:#f5f5fb;
  --line:#e4e6ec;
  --white:#ffffff;
  --footer:#121314;
}
*{box-sizing:border-box;margin:0;padding:0}
html,body{width:1200px;height:5164px;overflow:hidden}
body{position:relative;font-family:'Inter',sans-serif;color:var(--ink);background:var(--white)}
.abs{position:absolute}
a{color:inherit;text-decoration:none}
.tag{display:inline-flex;align-items:center;gap:6px;background:#eef0f7;border-radius:10px;padding:3px 10px;font-size:9px;font-weight:600;color:var(--green)}
.tag::before{content:"";width:5px;height:5px;border-radius:50%;background:var(--green)}
.accent{color:var(--green)}
.link{font-size:10px;font-weight:600;color:var(--green);border-bottom:1px solid var(--green);padding-bottom:2px}
.btn{display:inline-block;background:var(--green);color:#fff;font-size:10px;font-weight:600;padding:9px 16px;border-radius:4px}
.ph{border-radius:14px}
.brand{display:flex;align-items:center;gap:8px;font-weight:700;font-size:17px}
.brand i{width:22px;height:22px;border-radius:50%;background:var(--ink);display:block}

.nav{top:18px;left:222px;width:756px;height:26px;display:flex;align-items:center}
.nav ul{display:flex;list-style:none;gap:22px;margin-left:56px;font-size:11px;font-weight:500;color:#333}
.nav .active{border:2px solid var(--green);border-radius:14px;padding:4px 12px;margin:-6px -4px 0}
.nav .quote{margin-left:auto;font-size:10px;font-weight:600;color:var(--green);border-bottom:1px solid var(--green)}

.hero-title{top:150px;left:224px;font-size:47px;line-height:51px;font-weight:600;letter-spacing:-.5px}
.hero-sub{top:326px;left:224px;font-size:10px;color:#444}
.hero-cta{top:372px;left:224px;display:flex;align-items:center;gap:20px;font-size:10px}
.hero-cta .call{display:flex;align-items:center;gap:10px;color:#666}
.hero-cta .call b{font-weight:500;color:var(--green)}
.hero-cta .dot{width:26px;height:26px;border-radius:50%;background:var(--green);display:flex;align-items:center;justify-content:center}

.center{left:0;width:1200px;text-align:center}
.h2{font-size:27px;line-height:33px;font-weight:500;letter-spacing:-.3px}
.cards3{left:225px;width:750px;display:flex;gap:24px}
.svc{width:234px}
.svc .img{height:162px;position:relative}
.svc .badge{position:absolute;right:18px;bottom:-22px;width:58px;height:58px;border-radius:50%;background:#fff;border:6px solid #f3f3f7;display:flex;align-items:center;justify-content:center}
.svc h3{font-size:12px;font-weight:600;margin:28px 0 8px}
.svc p{font-size:9px;line-height:13px;color:#555;margin-bottom:16px;width:200px}
.note{font-size:8.5px;color:#777}
.note u{color:#333}

.stats{top:1140px;left:225px;width:750px;display:flex;justify-content:space-between;text-align:center}
.stat{width:250px}
.stat .num{font-size:86px;line-height:86px;font-weight:300;color:transparent;-webkit-text-stroke:1.4px var(--green)}
.stat .lbl{font-size:10px;color:var(--green);font-weight:500;margin-top:4px}

.about-band{top:1436px;left:0;width:1200px;height:574px;background:var(--green)}
.about-card{top:1338px;left:225px;width:750px;height:386px;background:var(--soft);border-radius:16px;overflow:hidden}
.about-copy{position:absolute;left:50px;top:100px;width:270px}
.about-copy .tag{width:270px;background:#fff}
.about-copy h2{font-size:27px;line-height:33px;font-weight:500;margin:14px 0 26px}
.about-img{position:absolute;right:0;top:0;width:375px;height:386px;background:linear-gradient(160deg,#1a5e4d,#7fa79b 55%,#cfe0da)}
.play{position:absolute;left:50%;top:50%;width:66px;height:66px;margin:-33px 0 0 -33px;border-radius:50%;background:#fff;display:flex;align-items:center;justify-content:center}
.mini{top:1748px}
.mini .card{width:234px;height:190px;background:#fff;border-radius:12px;padding:36px 32px}
.mini h3{font-size:12px;font-weight:600;margin:14px 0 8px}
.mini p{font-size:9px;line-height:13px;color:#555;margin-bottom:14px}

.testi{top:2266px;left:288px;width:624px;height:284px;background:var(--soft);border-radius:14px;overflow:hidden}
.testi blockquote{position:absolute;left:40px;top:90px;width:250px;font-size:12px;line-height:20px;font-weight:500}
.testi .who{position:absolute;left:40px;top:168px;font-size:9px;font-weight:600}
.testi .who span{display:block;font-weight:400;color:#888;font-size:8px;margin-top:3px}
.testi .photo{position:absolute;right:0;top:0;width:248px;height:284px;background:linear-gradient(180deg,#7a5a4a,#4c5563 70%,#2f3a46);border-radius:14px}
.dots{top:2574px;left:580px;display:flex;gap:7px}
.dots i{width:6px;height:6px;border-radius:50%;background:#ccc}
.dots i:first-child{background:#555}

.partners{top:2645px;left:0;width:1200px;height:96px;display:flex;border-top:1px solid var(--line);border-bottom:1px solid var(--line)}
.partners div{flex:1;border-right:1px solid var(--line);display:flex;align-items:center;justify-content:center;gap:6px;font-size:15px;font-weight:600;color:#8a8f98}
.partners i{width:12px;height:12px;border-radius:50%;background:#a4a9b1}

.app{top:2826px;left:225px;width:750px;height:386px;background:var(--soft);border-radius:16px;overflow:hidden}
.app .copy{position:absolute;left:50px;top:88px}
.app h2{font-size:27px;line-height:33px;font-weight:500;margin:14px 0 18px;width:290px}
.stores{display:flex;gap:12px}
.stores i{width:82px;height:28px;background:#000;border-radius:5px;display:block}
.stores i+i{width:92px}
.app .panel{position:absolute;right:0;top:0;width:375px;height:386px;background:var(--green);border-radius:16px}

.blog-band{top:3300px;left:0;width:1200px;height:695px;background:var(--soft)}
.post{width:236px}
.post .img{height:150px;border-radius:8px}
.post .date{display:inline-block;margin:18px 0 12px;border:1px solid #ccc;border-radius:12px;padding:4px 10px;font-size:8px;color:#555}
.post h3{font-size:12px;line-height:17px;font-weight:600;margin-bottom:28px;min-height:34px}

.contact{top:4045px;left:225px;width:750px;height:386px;background:var(--soft);border-radius:16px}
.contact .panel{position:absolute;left:0;top:0;width:324px;height:386px;background:var(--green);border-radius:16px;color:#fff;padding:72px 50px}
.contact .panel .tag{width:224px;background:#fff}
.contact .panel h2{font-size:27px;line-height:33px;font-weight:500;margin:12px 0 28px}
.contact .panel h2 span{color:#9fe3c9}
.contact .panel small{display:block;font-size:8px;margin-bottom:10px}
.contact .panel u{display:block;font-size:9px;color:#b6f0d8;margin-bottom:14px}
.form{position:absolute;left:412px;top:80px;width:300px}
.row{display:flex;gap:10px;margin-bottom:12px}
.field{flex:1}
.field label{display:block;font-size:8px;color:#777;margin-bottom:5px}
.field div{height:32px;border:1px solid #9aa0a8;border-radius:5px;background:#fff;font-size:9px;padding:10px 12px}
.field .area{height:66px}
.submit{display:block;height:30px;background:var(--green);color:#fff;border-radius:4px;text-align:center;font-size:10px;font-weight:600;line-height:30px}

.cta{top:4515px;left:0;width:1200px;height:392px;background:#00c483;overflow:hidden}
.cta h2{position:absolute;left:225px;top:140px;font-size:30px;line-height:36px;font-weight:500;color:#fff}
.cta h2 span{color:#9cf1cd}
.cta .btn{position:absolute;left:225px;top:242px;background:#fff;color:var(--green)}

.footer{top:4907px;left:0;width:1200px;height:257px;background:var(--footer);color:#fff}
.footer .brand{position:absolute;left:225px;top:50px}
.footer .brand i{background:#fff}
.footer .about{position:absolute;left:225px;top:82px;width:290px;font-size:9px;line-height:15px;color:#ddd}
.footer .news{position:absolute;left:225px;top:165px;font-size:9px;font-weight:600}
.footer .input{margin-top:10px;width:275px;height:34px;border:1px solid #555;border-radius:18px;font-size:8px;color:#aaa;font-weight:400;padding:11px 16px;position:relative}
.footer .input b{position:absolute;right:-1px;top:-1px;width:34px;height:34px;border-radius:50%;background:var(--mint)}
.col{position:absolute;top:50px;font-size:9px}
.col h4{font-weight:600;font-size:9px;margin-bottom:10px}
.col li{list-style:none;color:#bbb;margin-bottom:8px}
.social{display:flex;gap:10px}
.social i{width:10px;height:10px;border-radius:50%;background:#888}
.footer .copy{position:absolute;left:225px;top:237px;font-size:8px;color:#888}
</style>
</head>
<body>

<header class="abs nav">
  <div class="brand"><i></i>Tenvora</div>
  <ul>
    <li class="active">Home</li><li>About</li><li>Services ▾</li><li>Drivers</li><li>News</li><li>Contact</li>
  </ul>
  <a class="quote" href="#">Request Drivers</a>
</header>

<svg class="abs" style="top:80px;left:0" width="1200" height="470" viewBox="0 0 1200 470">
  <path d="M1200 10 C1060 60 980 200 980 410 L1200 410 Z" fill="#2f3a36"/>
  <path d="M0 440 C250 370 520 315 820 250 L830 272 C540 330 260 390 0 460 Z" fill="var(--green)"/>
</svg>
<div class="abs" role="img" aria-label="White commercial truck cab and trailer, front three-quarter view" style="top:84px;left:790px;width:410px;height:400px;background:linear-gradient(135deg,#dfe7e3,#9fb3aa 60%,#56675f);border-radius:40px 0 0 40px"></div>
<h1 class="abs hero-title">On demand,<br>professional<br><span class="accent">Drivers.</span></h1>
<p class="abs hero-sub">Real Drivers | Real Standards | Real Results for every fleet.</p>
<div class="abs hero-cta">
  <a class="link" href="#">Request Drivers</a>
  <span class="call"><span class="dot"><svg width="12" height="12" viewBox="0 0 24 24"><path fill="#fff" d="M6.6 10.8a15 15 0 0 0 6.6 6.6l2.2-2.2a1 1 0 0 1 1-.25 11.4 11.4 0 0 0 3.6.6 1 1 0 0 1 1 1V20a1 1 0 0 1-1 1A17 17 0 0 1 3 4a1 1 0 0 1 1-1h3.5a1 1 0 0 1 1 1c0 1.25.2 2.45.57 3.57a1 1 0 0 1-.25 1z"/></svg></span>Call us: <b>+1 555 210 4470</b></span>
</div>

<div class="abs center" style="top:618px"><span class="tag">Our Services</span></div>
<h2 class="abs center h2" style="top:648px">From long-haul routes to<br>local runs,<br><span class="accent">we supply drivers you can trust.</span></h2>
<div class="abs cards3" style="top:751px">
  <article class="svc">
    <div class="img ph" role="img" aria-label="Tractor-trailer on an open interstate" style="background:linear-gradient(180deg,#5a8fd0,#c8daf0)"><span class="badge"><svg width="18" height="18" viewBox="0 0 24 24"><path d="M4 6h10v10H4zM14 10h4l2 3v3h-6M7 19a1.5 1.5 0 1 0 0-.1M17 19a1.5 1.5 0 1 0 0-.1" fill="none" stroke="#12876a" stroke-width="1.6"/></svg></span></div>
    <h3>Long-Haul Drivers</h3><p>CDL Class A drivers ready for multi-day, over-the-road routes.</p><a class="link" href="#">Learn more</a>
  </article>
  <article class="svc">
    <div class="img ph" role="img" aria-label="Delivery trucks lined up at a regional depot" style="background:linear-gradient(160deg,#14527a,#2a7fa3 50%,#c2563e)"><span class="badge"><svg width="18" height="18" viewBox="0 0 24 24"><path d="M12 21s-7-6-7-11a7 7 0 0 1 14 0c0 5-7 11-7 11zM12 12a2 2 0 1 0 0-.1" fill="none" stroke="#12876a" stroke-width="1.6"/></svg></span></div>
    <h3>Regional &amp; Local</h3><p>Day-shift and dedicated local drivers for your regular lanes.</p><a class="link" href="#">Learn more</a>
  </article>
  <article class="svc">
    <div class="img ph" role="img" aria-label="Red truck moving fast on a highway" style="background:linear-gradient(170deg,#7fa0d4,#c7303a 55%,#5b6066)"><span class="badge"><svg width="18" height="18" viewBox="0 0 24 24"><path d="M12 3a9 9 0 1 0 0.1 0M12 7v5l3 2" fill="none" stroke="#12876a" stroke-width="1.6"/></svg></span></div>
    <h3>On-Demand Cover</h3><p>Short-notice drivers to cover sick days, peaks and vacancies.</p><a class="link" href="#">Learn more</a>
  </article>
</div>
<p class="abs center note" style="top:1044px">Carriers get vetted drivers fast. Drivers get steady, well-paid work. <u>See how it works.</u></p>

<div class="abs stats">
  <div class="stat"><div class="num">99%</div><div class="lbl">Shifts filled on time</div></div>
  <div class="stat"><div class="num">13</div><div class="lbl">Years of experience</div></div>
  <div class="stat"><div class="num">570</div><div class="lbl">Drivers on our roster</div></div>
</div>

<div class="abs about-band"></div>
<svg class="abs" style="top:1700px;left:0" width="1200" height="310" viewBox="0 0 1200 310"><path d="M215 310 L1200 20 L1200 310 Z" fill="var(--mint)"/></svg>
<section class="abs about-card">
  <div class="about-copy">
    <span class="tag">About us</span>
    <h2>Real drivers,<br>real standards,<br><span class="accent">real results.</span></h2>
    <a class="btn" href="#">Learn more</a>
  </div>
  <div class="about-img" role="img" aria-label="Truck terminal with loading docks, green tint"><span class="play"><svg width="12" height="12" viewBox="0 0 10 10"><path d="M2 1l7 4-7 4z" fill="#12876a"/></svg></span></div>
</section>
<div class="abs cards3 mini">
  <div class="card"><svg width="22" height="22" viewBox="0 0 24 24"><path d="M4 20V8l8-4 8 4v12zM9 20v-6h6v6" fill="none" stroke="#12876a" stroke-width="1.5"/></svg><h3>For trucking companies</h3><p>Tell us your lanes and dates,<br>we send qualified drivers.</p><a class="link" href="#">Request drivers</a></div>
  <div class="card"><svg width="22" height="22" viewBox="0 0 24 24"><path d="M12 12a4 4 0 1 0 0-.1M4 21c1-4 4-6 8-6s7 2 8 6" fill="none" stroke="#12876a" stroke-width="1.5"/></svg><h3>For drivers</h3><p>Find contract work that fits<br>your schedule and your CDL.</p><a class="link" href="#">Apply to drive</a></div>
  <div class="card"><svg width="22" height="22" viewBox="0 0 24 24"><path d="M12 3l8 3v6c0 5-4 8-8 9-4-1-8-4-8-9V6zM8 12l3 3 5-6" fill="none" stroke="#12876a" stroke-width="1.5"/></svg><h3>Safety &amp; compliance</h3><p>Every driver screened, licensed<br>and checked before dispatch.</p><a class="link" href="#">Learn more</a></div>
</div>

<div class="abs center" style="top:2104px"><span class="tag">Testimonials</span></div>
<h2 class="abs center h2" style="top:2134px">Discover what carriers and<br>drivers<br>are <span class="accent">saying about us.</span></h2>
<section class="abs testi">
  <blockquote>We needed three drivers by Monday. Tenvora had them on our trucks by Sunday night.</blockquote>
  <div class="who">Dana R.<span>Fleet Manager</span></div>
  <div class="photo" role="img" aria-label="Portrait photo of a client"></div>
</section>
<div class="abs dots"><i></i><i></i><i></i></div>

<div class="abs partners">
  <div><i></i>Orbita</div><div><i></i>Halvik</div><div><i></i>Quenta</div><div><i></i>Marlow</div><div><i></i>Fernhill</div>
</div>

<section class="abs app">
  <div class="copy">
    <span class="tag" style="background:#fff">Download app</span>
    <h2>Grab our app to book drivers or pick up shifts on the go.</h2>
    <div class="stores"><i></i><i></i></div>
  </div>
  <div class="panel"></div>
</section>

<div class="abs blog-band"></div>
<div class="abs center" style="top:3392px"><span class="tag" style="background:#fff">From Blog</span></div>
<h2 class="abs center h2" style="top:3422px">Discover the latest<br>tips,<br><span class="accent">for fleets and drivers.</span></h2>
<div class="abs cards3" style="top:3555px;gap:20px">
  <article class="post"><div class="img" role="img" aria-label="Row of trucks parked at a yard" style="background:linear-gradient(160deg,#8cc2ea,#e2a23a 55%,#b8412f)"></div><span class="date">November 7, 2022</span><h3>How contract drivers keep your fleet moving</h3><a class="link" href="#">Read more</a></article>
  <article class="post"><div class="img" role="img" aria-label="Driver checking a truck before a shift" style="background:linear-gradient(160deg,#3a2f2a,#d8612a 55%,#6a5a4a)"></div><span class="date">January 10, 2023</span><h3>Pre-trip checks every professional driver should know</h3><a class="link" href="#">Read more</a></article>
  <article class="post"><div class="img" role="img" aria-label="Aerial view of trucks parked at a depot" style="background:linear-gradient(160deg,#5c6b62,#9aa5a0 55%,#3d4a44)"></div><span class="date">February 14, 2023</span><h3>Finding steady CDL work on your own terms</h3><a class="link" href="#">Read more</a></article>
</div>
<div class="abs center" style="top:3865px"><a class="btn" href="#">Browse All Articles</a></div>

<section class="abs contact">
  <div class="panel">
    <span class="tag">Contact us</span>
    <h2>Need drivers or<br>want to drive?<br><span>Talk to us today.</span></h2>
    <small>Email</small><u>hello@tenvora-mail.com</u>
    <small>Phone</small><u>+1 555 301 2290</u>
  </div>
  <form class="form">
    <div class="row"><div class="field"><label>Name</label><div>John Doe</div></div><div class="field"><label>Email</label><div>contact@email.com</div></div></div>
    <div class="row"><div class="field"><label>Phone</label><div>+1 555-0142</div></div><div class="field"><label>I am a</label><div>Carrier / Driver</div></div></div>
    <div class="row"><div class="field"><label>Message</label><div class="area">Tell us about your routes or experience...</div></div></div>
    <span class="submit">Get in Touch</span>
  </form>
</section>

<section class="abs cta">
  <svg class="abs" style="top:0;left:0" width="1200" height="392" viewBox="0 0 1200 392"><path d="M200 392 C420 200 700 90 1200 40 L1200 392 Z" fill="var(--green)"/></svg>
  <div class="abs" role="img" aria-label="Truck trailer being coupled at a loading yard" style="left:850px;top:10px;width:350px;height:382px;background:linear-gradient(160deg,#cfd8d4,#8d9d96 60%,#5a6a64);border-radius:40px 0 0 0"></div>
  <h2>Short on drivers?<br><span>Book a professional now.</span></h2>
  <a class="btn" href="#">Request Drivers</a>
</section>

<footer class="abs footer">
  <div class="brand"><i></i>Tenvora</div>
  <p class="about">Tenvora – On Demand, Professional Drivers.<br>Real Drivers | Real Standards | Real Results</p>
  <div class="news">Sign up for our newsletter<div class="input">Enter your email...<b></b></div></div>
  <div class="col" style="left:568px"><h4>Navigation</h4><ul><li>Home</li><li>About</li><li>Services</li><li>Drivers</li><li>News</li><li>Contact</li></ul></div>
  <div class="col" style="left:690px"><h4>Services</h4><ul><li>Long-Haul Drivers</li><li>Regional &amp; Local</li><li>On-Demand Cover</li></ul></div>
  <div class="col" style="left:872px"><h4>Find us</h4><div class="social"><i></i><i></i><i></i><i></i></div></div>
  <p class="copy">© Tenvora. All rights reserved.</p>
</footer>

</body>
</html>
```